Letterhead Design Project

Based on the attached logo we would like have a designed of stationary.
As we are a management consulting company focused on business development dealing with C-level and one level below we new business cards.
We have decided to use KRM (Northvale Advisory Partners) as the business name. The legal name will be Northvale Advisory Partners ApS but we will brand us under KRM. The tack line is “Shaping Lasting Gains” if we need one.
For legal reasons we need to have the legal name on the letters together with the company no. (cvr. nr. 58190476)
We want to signal the following:
- Serious
- Professional
- Creating Result
- Capable of thinking out of the box and creative
- Fast reactions we will be there when needed
What we do not want to be view as is:
- To smart
- We know better
- We can fix it yesterday
Our Value Proposition is two sited:
- Increasing revenue
- Reduced sales cost or increased efficiency
Therefore, companies can call us when they want to grow or they need to be more efficient.
Our business cards should have a two sided print with the logo incl. the tack line on one side and the detailed information on the other site.
We need to have the following information on the letter head:
- Legal company name
- Cvr nr.
- Address incl. country name (Denmark)
- Main number
- Wed address
Symbols are welcome to be used to guide for the above information.
The following information are expected to be in the personal signature of the letter.
- Name
- Title
- Mobile number
- E-mail address
Updates
Some of you has requested our specific details so here they come:
- Address incl. country name (Denmark): Lyngholmvej 42, 3460 Birkerød, Denmark
- Main number: +45 7381 5502
- Wed address: www.krmgrowth.com
Mobile no. are +45 xxxx xxxx or +45 2857 3016
Our e-mail looks like this: firstname.seconname@KRMGROWTH.COM or for me: henrik.dalgaard@krmgrowth.com
We need the design (file) as finish as posible so we just need to add personal details before printing.
Please be aware that we will prefer designs where we can print the full letter incl. design. As we are communicating on e-mails with pdf versions of the letter we also need to have a design which will print on the clients printers.
Target Market(s)
C level and one level below.
Major local and international Companies.
Industry/Entity Type
Management Consulting
Font styles to use
Colors
Designer to choose colors to be used in the design.
Requirements
Must have
- Use of our logo without tack line

```html
<!DOCTYPE html>
<html lang="en">
<head>
<meta charset="utf-8">
<title>KRM Stationery</title>
<link href="https://fonts.googleapis.com/css2?family=Ubuntu:wght@400;500&display=swap" rel="stylesheet">
<style>
  :root {
    --brand-blue: #0a5fae;
    --brand-blue-light: #6ab4e8;
    --brand-orange: #f7941e;
    --paper: #ffffff;
    --edge: #3a3a3a;
    --stage: #aeada9;
    --text-font: "Ubuntu", sans-serif;
  }
  * { margin: 0; padding: 0; box-sizing: border-box; }
  html, body { width: 1200px; height: 1000px; overflow: hidden; }
  body { position: relative; background: var(--stage); font-family: var(--text-font); }

  .sheet { position: absolute; background: var(--paper); border: 1px solid var(--edge); }
  .abs { position: absolute; }
  .wordmark { position: absolute; color: var(--brand-blue); font-weight: 500; letter-spacing: -0.5px; line-height: 1; }
  .blue-band { position: absolute; background: linear-gradient(90deg, var(--brand-blue) 0%, #1471c0 35%, var(--brand-blue-light) 58%, #1471c0 75%, var(--brand-blue) 100%); }
  .orange-block { position: absolute; background: var(--brand-orange); }

  /* Letterhead */
  .letterhead { left: 95px; top: 34px; width: 496px; height: 712px; }
  .letterhead .wordmark { left: 24px; top: 28px; font-size: 38px; }
  .letterhead .orange-block { left: 139px; top: 25px; width: 27px; height: 32px; }
  .letterhead .blue-band { left: 173px; top: 24px; width: 322px; height: 33px; }
  .letterhead .band-info { position: absolute; right: 24px; top: 1px; color: #fff; font-size: 8px; line-height: 10px; text-align: right; }
  .letterhead .tagline { position: absolute; right: 25px; bottom: 14px; color: var(--brand-orange); font-size: 13px; }

  /* Business card front */
  .card-front { left: 826px; top: 34px; width: 308px; height: 177px; background: var(--brand-orange); }
  .card-front .wordmark { left: 0; width: 100%; text-align: center; top: 34px; font-size: 56px; }
  .card-front .tagline { position: absolute; left: 0; width: 100%; text-align: center; top: 126px; font-size: 17px; color: var(--brand-blue); }

  /* Business card back */
  .card-back { left: 626px; top: 197px; width: 308px; height: 176px; }
  .card-back .orange-block { left: 0; top: 15px; width: 11px; height: 32px; }
  .card-back .wordmark { left: 18px; top: 14px; font-size: 34px; }
  .card-back .blue-band { left: 118px; top: 15px; width: 189px; height: 32px; }
  .card-back .person-name { position: absolute; right: 18px; top: 7px; color: #fff; font-size: 15px; }
  .card-back .person-title { position: absolute; right: 18px; top: 52px; color: var(--brand-blue); font-size: 12px; }
  .contact-list { position: absolute; left: 26px; top: 94px; list-style: none; }
  .contact-list li { display: flex; align-items: center; height: 15.5px; color: var(--brand-blue); font-size: 12px; }
  .contact-list svg { width: 12px; height: 12px; margin-right: 11px; fill: none; stroke: var(--brand-blue); stroke-width: 1.4; }

  /* Envelope */
  .envelope { left: 550px; top: 384px; width: 611px; height: 303px; }
  .sender { position: absolute; left: 45px; top: 24px; color: var(--brand-orange); font-size: 12px; line-height: 16.3px; }
  .sender .legal-name { font-size: 11px; font-weight: 500; }
  .envelope .orange-block { left: 0; top: 187px; width: 32px; height: 94px; }
  .envelope .wordmark { left: 40px; top: 195px; font-size: 46px; }
  .envelope .tagline { position: absolute; left: 49px; top: 262px; font-size: 12px; color: var(--brand-blue); }
  .envelope .blue-band { left: 189px; top: 187px; width: 421px; height: 94px; }
  .address-window { position: absolute; left: 178px; top: 4px; width: 189px; height: 82px; background: #fff; border-radius: 10px; display: flex; align-items: center; justify-content: center; color: var(--brand-blue); font-size: 12px; }
</style>
</head>
<body>

  <section class="sheet letterhead" aria-label="Letterhead">
    <div class="wordmark">KRM</div>
    <div class="orange-block"></div>
    <div class="blue-band">
      <div class="band-info">Company Address<br>www.companysite.com<br>123-456-7890</div>
    </div>
    <p class="tagline">Shaping Lasting Gains</p>
  </section>

  <section class="sheet card-front" aria-label="Business card front">
    <div class="wordmark">KRM</div>
    <p class="tagline">Shaping Lasting Gains</p>
  </section>

  <section class="sheet card-back" aria-label="Business card back">
    <div class="orange-block"></div>
    <div class="wordmark">KRM</div>
    <div class="blue-band"><span class="person-name">Name Person</span></div>
    <p class="person-title">President</p>
    <ul class="contact-list">
      <li><svg viewBox="0 0 12 12"><rect x="3" y="0.8" width="6" height="10.4" rx="1"/><line x1="5" y1="9.3" x2="7" y2="9.3"/></svg>123-123-1234</li>
      <li><svg viewBox="0 0 12 12"><rect x="1" y="3" width="10" height="7.5"/><polyline points="1,3 6,7.5 11,3"/></svg>name@companysite.com</li>
      <li><svg viewBox="0 0 12 12"><rect x="2" y="2" width="8" height="6"/><line x1="0.5" y1="10.3" x2="11.5" y2="10.3"/></svg>www.companysite.com</li>
      <li><svg viewBox="0 0 12 12"><path d="M6 11.3 C3.5 7.8 3 6.6 3 4.6 A3 3 0 0 1 9 4.6 C9 6.6 8.5 7.8 6 11.3Z" fill="#0a5fae"/><circle cx="6" cy="4.6" r="1" fill="#fff" stroke="none"/></svg>Anywhere, Denmark</li>
    </ul>
  </section>

  <section class="sheet envelope" aria-label="Envelope">
    <address class="sender" style="font-style:normal">
      <span class="legal-name">Northvale Advisory Partners ApS</span><br>
      123-123-1234<br>
      cvr. nr. 58190476<br>
      Anywhere, Denmark<br>
      www.companysite.com
    </address>
    <div class="orange-block"></div>
    <div class="wordmark">KRM</div>
    <p class="tagline">Shaping Lasting Gains</p>
    <div class="blue-band">
      <div class="address-window">John Doe</div>
    </div>
  </section>

</body>
</html>
```